Pill bottle label - clearly defined niche

UPDATE 02/01/19 - VERY IMPORTANT - SEE LATEST ATTACHMENT FOR A SIGNIFICANT UPDATE TO THE BRIEF - Word Doc: "Brief Update V1.3"

I need a striking design for a vitamin/supplement bottle. The purpose of the supplement is to help the body fight the effects of airborne pollution. It will initially be targeted to the China market. The product will be named Haze Warden. I want to get away from the generic look of vitamin bottles and use an illustrated character, probably an animal, as I think it is more memorable and gender neutral. The strap line will be "Fight" or more likely, "Fight Back".The product will contain a combination of B, C, D & E vitamins AND Traditional Chinese Medicine (TCM) ingredients such as ginseng, astragalus and ginkgo leaf. Therefore, we need to say that this product is bringing together the best of East and West to protect against the effects of smog.Recap of elements;Name: Haze WardenStrap Line: Fight Back(the name and strap will also need to appear in Chinese (maybe in a narrow band around the top of the label?)Character: Illustration of cute Chinese fighting character (human or animal) OR maybe a giraffe with his head above the smog clouds. Wide open to ideas.Company Name: just put ORVIN Ltd. for now!Ingredients panel, Barcode, QR codeOther sources for visual inspiration are air-pollution apps - most popular one is Sky Ledger sky-ledger.example.I have a Snapboard page where I've saved some nice bottle/label designs and some visuals that might inspire for the character - https://www.snapboard.example/tolandreeve/packaging/vitamins/
Updates

Bad time of year with Christmas and New Year affecting our timeline. To get more designs and have the time to review and respond we need to allow more time. Even the 4th is a bit tight with new years eve/day in the middle of it. Ideally, I would make the deadline the 7th, which would allow that weekend to be included.

Please ensure you view the latest brief update (attached as a Word doc) in Projects.

Target Market(s)

Chinese consumers

Industry/Entity Type

Supplement

Requirements
Must have
• UPDATE 02/01/19 - VERY IMPORTANT - SEE LATEST ATTACHMENT FOR A SIGNIFICANT UPDATE TO THE BRIEF
• Brief V1.2
• In terms of strategic marketing message conveyed by the strap line, I have two different routes we could go down.
• The first is the more "aggressive" route (fight back), currently symbolised by the fighting character.
• The second is the "clever" route, currently symbolised by the giraffe with its head above the smog clouds. The "fight back" strap line will not work with the giraffe. If we were to go down the "smart" route, we will use a strap line like "Be Smart"
• There may be a third route which combines the two approaches. If we were to have a strap line of "Fight Smart" it might be possible to use the gentle intelligent giraffe character but add a martial arts headband.
• Looking at the imagery - I like this one. That doesn't mean you have to use it! I still want to see creativity and originality. But, a stylised version with a giraffe in a headband and another with sunglasses on, might work well. I could see the bottom half of the label being cloudy and murky and it being bright and sunny up top.
Nice to have

```html
<!DOCTYPE html>
<html lang="en">
<head>
<meta charset="UTF-8">
<title>Haze Warden – Dietary Supplement Label</title>
<link rel="stylesheet" href="https://fonts.googleapis.com/css2?family=Montserrat:ital,wght@0,300;0,400;0,600;0,700;1,800;1,900&family=Noto+Sans+SC:wght@300&display=swap">
<style>
  :root {
    --backdrop: #dcdcdc;
    --label-charcoal: #25282c;
    --band-red: #d8262f;
    --title-red: #e0262e;
    --sun-orange: #f58a4a;
    --ink-dark: #2a2320;
    --text-white: #ffffff;
    --text-soft: #e6e6e6;
    --giraffe-orange: #e98d3a;
  }
  * { margin: 0; padding: 0; box-sizing: border-box; }
  html, body {
    width: 1200px; height: 859px; overflow: hidden;
    background: var(--backdrop);
  }
  .label {
    position: absolute; left: 362px; top: 90px;
    width: 476px; height: 680px;
    background: var(--label-charcoal);
    overflow: hidden;
    font-family: "Montserrat", sans-serif;
  }
  .strap-band {
    position: absolute; left: 0; top: 0;
    width: 74px; height: 100%;
    background: var(--band-red);
  }
  .strap-band__text {
    position: absolute; left: 37px; top: 340px;
    width: 680px;
    transform: translate(-50%, -50%) rotate(-90deg);
    display: flex; align-items: center; justify-content: flex-start;
    gap: 30px; padding-left: 40px;
    white-space: nowrap;
    color: var(--text-white);
  }
  .strap-band__chinese {
    font-family: "Noto Sans SC", sans-serif;
    font-weight: 300; font-size: 34px; letter-spacing: 2px;
  }
  .strap-band__english {
    font-style: italic; font-weight: 900;
    font-size: 38px; letter-spacing: 1px;
  }
  .sun-badge {
    position: absolute; left: 276px; top: -34px;
    width: 196px; height: 196px; border-radius: 50%;
    background: var(--sun-orange);
    display: flex; flex-direction: column; justify-content: flex-end;
    padding: 0 24px 38px 34px;
    color: var(--ink-dark);
    font-weight: 600; font-size: 13.5px; line-height: 1.2;
  }
  .character-art {
    position: absolute; left: 118px; top: 24px;
    width: 352px; height: 308px;
  }
  .product-name {
    position: absolute; left: 100px; top: 350px;
    font-style: italic; font-weight: 900;
    line-height: 0.95; letter-spacing: 0;
    white-space: nowrap;
  }
  .product-name__first {
    display: block; color: var(--text-white); font-size: 92px;
  }
  .product-name__second {
    display: block; color: var(--title-red); font-size: 60px;
    margin-left: 8px;
  }
  .product-type {
    position: absolute; left: 104px; top: 530px;
    color: var(--text-white);
    font-weight: 700; font-size: 23px; letter-spacing: 0.5px;
  }
  .product-count {
    position: absolute; left: 156px; top: 578px;
    color: var(--text-soft);
    font-weight: 400; font-size: 24px;
  }
</style>
</head>
<body>
  <div class="label">
    <div class="strap-band">
      <div class="strap-band__text">
        <span class="strap-band__chinese" lang="zh">霾守卫者</span>
        <span class="strap-band__english">FIGHT SMARTER</span>
      </div>
    </div>

    <svg class="character-art" viewBox="0 0 352 308" role="img" aria-label="Illustration of a giraffe with a colourful patterned neck rising its head above grey smog clouds">
      <defs>
        <linearGradient id="giraffeTone" x1="0" y1="0" x2="0.6" y2="1">
          <stop offset="0" stop-color="var(--giraffe-orange)"/>
          <stop offset="0.6" stop-color="#c9673a"/>
          <stop offset="1" stop-color="var(--label-charcoal)"/>
        </linearGradient>
        <linearGradient id="cloudTone" x1="0" y1="0" x2="0" y2="1">
          <stop offset="0" stop-color="#9a9da2"/>
          <stop offset="1" stop-color="var(--label-charcoal)"/>
        </linearGradient>
      </defs>
      <rect x="40" y="0" width="150" height="300" rx="40" fill="url(#giraffeTone)" opacity="0.85"/>
      <rect x="0" y="170" width="352" height="130" rx="60" fill="url(#cloudTone)" opacity="0.7"/>
    </svg>

    <div class="sun-badge">
      <p>Best of East &amp; West<br>Vitamins B, C, D &amp; E<br>with TCM<br>Ginseng, Astragalus<br>&amp; Ginko Leaf</p>
    </div>

    <h1 class="product-name">
      <span class="product-name__first">HAZE</span>
      <span class="product-name__second">WARDEN</span>
    </h1>
    <p class="product-type">DIETARY SUPPLEMENT</p>
    <p class="product-count">60 Capsules</p>
  </div>
</body>
</html>
```